Business Card Design for Cybersecurity Company - Quorvent Systems

We need a business card design for our new cybersecurity company, Quorvent. We’re going for a clean, hi tech look that feels modern, premium, and trustworthy. We want a design that really stands out and makes people say WOW when we hand it over!

Quorvent delivers reliable IT support and managed services for small and mid sized businesses. We help companies stay secure, efficient, and connected through proactive monitoring, cybersecurity services, cloud management, and remote support.

Target Market(s)

Designers should target small and mid sized businesses that need dependable cybersecurity and IT support.

Industry/Entity Type

Cybersecurity, Managed Service Provider, IT services

Contact Information for Business Card

Contact information

Requirements
Must have
• The card should look clean, modern, and tech focused, with the Quorvent logo, clear contact info, and strong readability. It needs to feel premium and professional while still keeping a simple layout that fits a cybersecurity and IT brand.
Nice to have
• Nice to have elements include subtle touches that give the card a modern, tech feel, along with a layout that works well in different background styles.
Should not have
• The card should avoid clutter, loud graphics, or anything that takes attention away from the logo and contact details.

```html
<!DOCTYPE html>
<html lang="en">
<head>
<meta charset="utf-8">
<title>Quorvent Systems – Business Card</title>
<link rel="stylesheet" href="https://fonts.googleapis.com/css2?family=Roboto:wght@300;400;500;700&display=swap">
<style>
  :root {
    --page-bg: #e6e7ea;
    --card-shadow: rgba(0, 0, 0, 0.28);
    --front-violet: #6a4aa8;
    --front-mid: #4f64b6;
    --front-blue: #3f80c8;
    --front-text: #ffffff;
    --front-text-soft: #e8ecfb;
    --circuit-light: #5a74c6;
    --circuit-deep: #5a4db0;
    --back-bg: #ffffff;
    --brand-ink: #161821;
    --brand-accent: #5561c0;
  }
  * { box-sizing: border-box; margin: 0; padding: 0; }
  html, body {
    width: 1200px;
    height: 1200px;
    overflow: hidden;
    background: var(--page-bg);
    font-family: "Roboto", Arial, sans-serif;
  }
  .sheet {
    position: relative;
    width: 1200px;
    height: 1200px;
  }
  .card {
    position: absolute;
    left: 150px;
    width: 900px;
    height: 525px;
    overflow: hidden;
    box-shadow: 14px 14px 18px var(--card-shadow);
  }
  /* Front */
  .card-front {
    top: 55px;
    background: linear-gradient(30deg, var(--front-violet) 0%, var(--front-mid) 45%, var(--front-blue) 100%);
    color: var(--front-text);
  }
  .circuit-art {
    position: absolute;
    top: 0;
    right: 0;
    width: 312px;
    height: 525px;
    background: linear-gradient(200deg, var(--circuit-light) 0%, var(--circuit-deep) 100%);
    opacity: 0.55;
  }
  .holder-name {
    position: absolute;
    left: 62px;
    top: 108px;
    font-size: 36px;
    font-weight: 700;
    letter-spacing: 0.5px;
    line-height: 1;
  }
  .holder-role {
    position: absolute;
    left: 62px;
    top: 163px;
    font-size: 22px;
    font-weight: 300;
    color: var(--front-text-soft);
  }
  .contact-list {
    position: absolute;
    left: 62px;
    top: 302px;
    list-style: none;
    font-size: 23px;
    font-weight: 300;
    color: var(--front-text-soft);
  }
  .contact-list li {
    height: 41.5px;
    line-height: 32px;
  }
  .contact-list .label {
    font-weight: 500;
    color: var(--front-text);
  }
  /* Back */
  .card-back {
    top: 619px;
    background: var(--back-bg);
  }
  .brand-lockup {
    position: absolute;
    left: 0;
    right: 0;
    top: 228px;
    display: flex;
    align-items: center;
    justify-content: center;
    gap: 22px;
  }
  .brand-mark {
    width: 58px;
    height: 58px;
    background: var(--brand-accent);
  }
  .brand-name {
    font-size: 60px;
    font-weight: 500;
    color: var(--brand-ink);
    letter-spacing: 1px;
    line-height: 1;
  }
</style>
</head>
<body>
  <main class="sheet">
    <section class="card card-front" aria-label="Card front">
      <div class="circuit-art" role="img" aria-label="Decorative circuit-trace pattern in violet and blue"></div>
      <h1 class="holder-name">DANA ROURKE</h1>
      <p class="holder-role">Owner | CEO | Quorvent Systems</p>
      <ul class="contact-list">
        <li><span class="label">P:</span> (855) 304-7729</li>
        <li><span class="label">M:</span> (555) 214-0387</li>
        <li><span class="label">E:</span> dana@quorvent.com</li>
        <li><span class="label">W:</span> quorvent.com</li>
      </ul>
    </section>

    <section class="card card-back" aria-label="Card back">
      <div class="brand-lockup">
        <span class="brand-mark" aria-hidden="true"></span>
        <span class="brand-name">Quorvent Systems</span>
      </div>
    </section>
  </main>
</body>
</html>
```